Lifestyle brand needs lip balm label design

We need a label design for lip balm tubes. The name of our company is "lorvanquill"

Design Description:
Our lip balm tubes will be black. The label itself will be clear/transparent. We would like to create a gradient effect with the color green (same shade as our logo) starting from the bottom and slowly fading out to clear so that the black tube is visible (example of gradient shown in attached image)

We have two lip balm flavors: mint and lemongrass.
We would like the top/clear portion of the label to say "MINT" (all caps) . The second label should say "LEMONGRASS" (all caps) in the same location. Our logo "lorvanquill" should be in the bottom/green portion of the label. Below the logo, we would like the words "NATURAL BALM" (all caps) in white text

```html
<!DOCTYPE html>
<html lang="en">
<head>
<meta charset="utf-8">
<title>lorvanquill Natural Balm — Mint Label</title>
<link rel="stylesheet" href="https://fonts.googleapis.com/css2?family=Josefin+Sans:wght@300&family=Montserrat:wght@300;700&display=swap">
<style>
  :root {
    --page-bg: #e8e8e8;
    --leaf-green: #609545;
    --tube-black: #000000;
    --label-white: #ffffff;
  }
  html, body {
    margin: 0;
    padding: 0;
    width: 1200px;
    height: 960px;
    overflow: hidden;
    background: var(--page-bg);
  }
  .canvas {
    position: relative;
    width: 1200px;
    height: 960px;
  }
  .balm-label {
    position: absolute;
    left: 160px;
    top: 40px;
    width: 880px;
    height: 880px;
    display: block;
  }
  .label-green { fill: var(--leaf-green); }
  .label-band { fill: var(--tube-black); }
  .brand-name {
    font-family: "Josefin Sans", sans-serif;
    font-weight: 300;
    font-size: 130px;
    fill: var(--label-white);
  }
  .product-line {
    font-family: "Montserrat", sans-serif;
    font-weight: 700;
    font-size: 92px;
  }
  .product-line--natural { fill: var(--leaf-green); }
  .product-line--balm { fill: var(--label-white); }
  .flavour {
    font-family: "Montserrat", sans-serif;
    font-weight: 300;
    font-size: 34px;
    fill: var(--leaf-green);
  }
</style>
</head>
<body>
<main class="canvas">
  <svg class="balm-label" viewBox="0 0 1000 1000" xmlns="http://www.w3.org/2000/svg" aria-label="lorvanquill Natural Balm mint label">
    <rect class="label-green" x="0" y="0" width="1000" height="1000"/>
    <rect class="label-band" x="421" y="0" width="550" height="1000"/>

    <text class="brand-name" transform="translate(588 830) rotate(-90)" textLength="650" lengthAdjust="spacingAndGlyphs">lorvanquill</text>
    <text class="product-line product-line--natural" transform="translate(773 725) rotate(-90)" textLength="450" lengthAdjust="spacingAndGlyphs">NATURAL</text>
    <text class="product-line product-line--balm" transform="translate(873 630) rotate(-90)" textLength="262" lengthAdjust="spacingAndGlyphs">BALM</text>
    <text class="flavour" transform="translate(923 620) rotate(-90)" textLength="240" lengthAdjust="spacing">MINT</text>
  </svg>
</main>
</body>
</html>
```